Letterhead for paint manufacturing company

We need a letterhead for a paint manufacturing company called Corvane Industries Limited. We manufacture paint for construction companies as well as end consumers. We don't have a logo. Would like to see a design incorporating Pastel colours. We are based in Nigeria. Information to be included on the letterhead are:
Company name; Address: 12 plot D Amokwe Industrial Estate, Ilupeju, Ikeja; Phone numbers: 08061729350, 08072364918

Industry/Entity Type

Construction

```html
<!DOCTYPE html>
<html lang="en">
<head>
<meta charset="utf-8">
<title>Corvane Industries Limited — Stationery</title>
<link rel="stylesheet" href="https://fonts.googleapis.com/css2?family=Open+Sans:wght@400;600&display=swap">
<style>
  :root {
    --backdrop: #ececec;
    --paper: #ffffff;
    --ink: #3a3a3a;
    --ink-soft: #5a5a5a;
    --sky: #6ec8ea;
    --rose: #f09ab4;
    --magenta: #ec6fb3;
    --violet: #9a5fb0;
    --coral: #e2504a;
    --orange: #f0904a;
    --lime: #8cc63f;
    --sun: #f7d04a;
    --accent: #e94c7a;
  }
  * { box-sizing: border-box; margin: 0; padding: 0; }
  html, body { width: 1200px; height: 1000px; overflow: hidden; }
  body {
    background: var(--backdrop);
    font-family: "Open Sans", Arial, sans-serif;
    color: var(--ink);
    position: relative;
  }
  .sheet {
    position: absolute;
    top: 146px;
    width: 500px;
    height: 707px;
    background: var(--paper);
    box-shadow: 0 4px 18px rgba(0,0,0,0.12);
    overflow: hidden;
  }
  .folder-cover { left: 60px; }
  .letterhead { left: 640px; }

  /* Folder cover */
  .cover-artwork {
    position: absolute;
    left: 0; top: 0;
    width: 330px; height: 470px;
    border-radius: 0 0 160px 0;
    background: linear-gradient(160deg, var(--sky) 0%, var(--rose) 25%, var(--magenta) 45%, var(--violet) 65%, var(--coral) 82%, var(--orange) 100%);
    opacity: 0.9;
  }
  .brand {
    position: absolute;
    display: flex;
    align-items: center;
    gap: 8px;
    font-weight: 600;
    color: var(--ink);
    white-space: nowrap;
  }
  .brand-dot {
    border-radius: 50%;
    background: var(--magenta);
    flex: none;
  }
  .folder-cover .brand { right: 34px; bottom: 40px; font-size: 13px; }
  .folder-cover .brand-dot { width: 22px; height: 22px; }

  /* Letterhead */
  .letterhead .brand { right: 34px; top: 44px; font-size: 10px; }
  .letterhead .brand-dot { width: 16px; height: 16px; }
  .letter {
    position: absolute;
    left: 44px; top: 110px;
    width: 412px;
    font-size: 9.5px;
    line-height: 1.55;
    color: var(--ink-soft);
  }
  .letter p { margin-bottom: 12px; }
  .letter .salutation { color: var(--ink); margin-bottom: 10px; }
  .letter .closing { color: var(--ink); margin-bottom: 8px; }
  .signature {
    position: absolute;
    right: 60px; top: 430px;
    width: 150px; height: 40px;
    background: linear-gradient(90deg, rgba(58,58,58,0.08), rgba(58,58,58,0.16));
    border-radius: 4px;
  }
  .contact-bar {
    position: absolute;
    left: 44px; right: 34px; bottom: 104px;
    display: flex;
    flex-wrap: wrap;
    gap: 4px 14px;
    font-size: 7.5px;
    line-height: 1.3;
    color: var(--ink-soft);
  }
  .contact-item { display: flex; align-items: center; gap: 4px; white-space: nowrap; }
  .contact-item svg { width: 8px; height: 8px; flex: none; }
  .footer-pattern {
    position: absolute;
    left: 0; right: 0; bottom: 0;
    height: 86px;
    background: linear-gradient(90deg, var(--sky) 0%, var(--violet) 18%, var(--lime) 36%, var(--orange) 54%, var(--sun) 70%, var(--coral) 84%, var(--sky) 100%);
    opacity: 0.85;
  }
</style>
</head>
<body>

  <section class="sheet folder-cover">
    <div class="cover-artwork" role="img" aria-label="Flowing pastel paint ribbons in blue, pink, violet, red and orange"></div>
    <div class="brand">
      <span class="brand-dot"></span>
      <span class="brand-name">Corvane Industries Limited</span>
    </div>
  </section>

  <section class="sheet letterhead">
    <div class="brand">
      <span class="brand-dot"></span>
      <span class="brand-name">Corvane Industries Limited</span>
    </div>

    <div class="letter">
      <p class="salutation">Dear Client,</p>
      <p>Thank you for choosing our paints for your recent project. We are pleased to confirm that your order has been prepared and will be delivered to your site this week. Our team will contact you to agree a suitable time, and our technical staff remain available to advise on colour, coverage and surface preparation.</p>
      <p>Please find the invoice and product data sheets enclosed with this letter. Should you need more information on our interior and exterior ranges, or wish to arrange a visit to our factory, do not hesitate to reach us by phone or email. We look forward to working with you again.</p>
      <p class="closing">Best regards,</p>
    </div>

    <div class="signature" role="img" aria-label="Handwritten signature"></div>

    <div class="contact-bar">
      <span class="contact-item">
        <svg viewBox="0 0 10 10"><path d="M2 1 L4 1 L4.6 3.2 L3.4 4 Q4.4 6 6 6.6 L6.8 5.4 L9 6 L9 8 Q9 9 8 9 Q1 8.4 1 2 Q1 1 2 1Z" fill="var(--accent)"/></svg>
        555-0147-82
      </span>
      <span class="contact-item">
        <svg viewBox="0 0 10 10"><path d="M5 0.5 A3.3 3.3 0 0 1 8.3 3.8 Q8.3 6 5 9.5 Q1.7 6 1.7 3.8 A3.3 3.3 0 0 1 5 0.5Z" fill="var(--accent)"/><circle cx="5" cy="3.8" r="1.2" fill="#fff"/></svg>
        12 Plot D, Kestrel Industrial Estate, Amberfield
      </span>
      <span class="contact-item">
        <svg viewBox="0 0 10 10"><path d="M2 1 L4 1 L4.6 3.2 L3.4 4 Q4.4 6 6 6.6 L6.8 5.4 L9 6 L9 8 Q9 9 8 9 Q1 8.4 1 2 Q1 1 2 1Z" fill="var(--accent)"/></svg>
        555-0193-64
      </span>
      <span class="contact-item">
        <svg viewBox="0 0 10 10"><rect x="0.5" y="2" width="9" height="6" rx="1" fill="var(--accent)"/><path d="M0.8 2.4 L5 5.4 L9.2 2.4" stroke="#fff" stroke-width="0.8" fill="none"/></svg>
        hello@corvane-example.test
      </span>
      <span class="contact-item">
        <svg viewBox="0 0 10 10"><circle cx="5" cy="5" r="4.3" fill="none" stroke="var(--accent)" stroke-width="1"/><path d="M0.8 5 H9.2 M5 0.7 Q2.4 5 5 9.3 M5 0.7 Q7.6 5 5 9.3" stroke="var(--accent)" stroke-width="0.8" fill="none"/></svg>
        www.corvane-example.test
      </span>
    </div>

    <div class="footer-pattern" role="img" aria-label="Decorative mosaic band of pastel tiles in blue, violet, green, orange, yellow and red"></div>
  </section>

</body>
</html>
```